Website redesign for Maplecrest Drip Clinic

We need website redesign for Maplecrest Drip Clinic - Natural Health & Wellness Center.
In addition to our IV Infusions & Intramuscular Injection, our team offers a full spectrum of natural healing modalities to optimize physical, emotional and spiritual well being.
our current website is www.maplecrestdripcare.com
Our major competitor is https://brisknookhydra.com/
See uploaded design of current logo.
Target Market(s)
Health, fitness, functional medicine, immune boosting, alternative medicine, holistic medicine, supplements
Industry/Entity Type
Health And Wellness
Logo Text
Maplecrest Drip Clinic - Natural Health & Wellness Center
Number of Pages Required
5+ page
Requirements
Must have
- Contemporary Professional / Medical / Health Professional Look
Our current website is www.maplecrestdripcare.com

```html
<!DOCTYPE html>
<html lang="en">
<head>
<meta charset="utf-8">
<title>Maplecrest Drip Clinic – Natural Health &amp; Wellness</title>
<link href="https://fonts.googleapis.com/css2?family=Montserrat:wght@300;400;500;600&family=Open+Sans:wght@400;600;700;800&display=swap" rel="stylesheet">
<style>
:root{
  --navy:#1f2552;
  --navy-2:#2b3570;
  --green:#8fcb18;
  --green-2:#b5e02a;
  --lavender:#eceef9;
  --ink:#23284a;
  --muted:#5b5f78;
  --white:#ffffff;
}
*{margin:0;padding:0;box-sizing:border-box}
html,body{width:1200px;height:4418px;overflow:hidden}
body{font-family:'Montserrat',sans-serif;color:var(--ink);background:var(--white);position:relative}
.abs{position:absolute}
h1,h2,h3,h4{font-family:'Open Sans',sans-serif}

/* nav */
.site-header{position:absolute;left:0;top:0;width:1200px;height:108px;background:var(--white)}
.brand{position:absolute;left:43px;top:32px;display:flex;align-items:center;gap:12px}
.brand-dot{width:40px;height:40px;border-radius:50%;background:var(--navy)}
.brand-name{font-family:'Open Sans',sans-serif;font-weight:700;font-size:26px;color:var(--navy)}
.main-nav a{position:absolute;top:42px;font-size:16px;color:#3b3f55;text-decoration:none}
.main-nav a.active{font-weight:600;color:var(--ink)}
.cart{position:absolute;left:1118px;top:36px}

/* hero */
.hero{position:absolute;left:0;top:108px;width:1200px;height:629px;
  background:linear-gradient(90deg,#1b1c2c 0%,#3a3035 35%,#6b5a52 60%,#8a7a70 100%)}
.hero-shade{position:absolute;inset:0;background:linear-gradient(90deg,rgba(15,16,32,.85) 0%,rgba(15,16,32,.45) 50%,rgba(15,16,32,.1) 100%)}
.hero-title{position:absolute;left:103px;top:196px;font-size:48px;font-weight:700;color:var(--white);letter-spacing:-.5px}
.hero-title span{color:var(--green)}
.hero-sub{position:absolute;left:103px;top:252px;font-family:'Open Sans',sans-serif;font-size:34px;color:var(--white)}
.hero-text{position:absolute;left:107px;top:310px;font-size:16px;line-height:23px;color:#e8e8ef}
.btn{position:absolute;display:flex;align-items:center;justify-content:center;font-size:15px;font-weight:500;text-transform:uppercase;text-decoration:none}
.btn-outline-green{left:111px;top:382px;width:186px;height:51px;border:2px solid var(--green);color:var(--green)}
.arrow{position:absolute;top:264px}

/* welcome */
.welcome{position:absolute;left:0;top:737px;width:1200px;height:549px;background:var(--white)}
.welcome-photo{position:absolute;left:160px;top:50px;width:300px;height:420px;border-radius:150px 150px 150px 150px;background:linear-gradient(160deg,#7a7672 0%,#4b4a4e 55%,#2f2e32 100%)}
.welcome h2{position:absolute;left:556px;top:96px;font-size:31px;font-weight:700;color:var(--ink)}
.welcome .tagline{position:absolute;left:556px;top:140px;font-size:30px;font-weight:300;color:var(--ink)}
.welcome p{position:absolute;left:558px;top:200px;width:560px;font-size:16px;line-height:31.5px;color:#3d4158}
.btn-outline-navy{left:560px;top:384px;width:186px;height:51px;border:2px solid var(--navy);color:var(--navy)}

/* services */
.services{position:absolute;left:0;top:1286px;width:1200px;height:541px;background:linear-gradient(135deg,#1c2350 0%,#2c3571 60%,#3a4585 100%)}
.services h2{position:absolute;left:0;top:60px;width:1200px;text-align:center;font-size:31px;font-weight:700;color:var(--white)}
.service{position:absolute;top:148px;width:250px;text-align:center;color:var(--white)}
.service svg{display:block;margin:0 auto}
.service h3{margin-top:16px;font-size:19px;font-weight:700}
.service p{margin-top:10px;font-size:13px;line-height:21px;color:#dfe2f2}
.btn-outline-white{left:509px;top:440px;width:186px;height:52px;border:2px solid var(--white);color:var(--white)}

/* packages */
.packages{position:absolute;left:0;top:1827px;width:1200px;height:636px;background:var(--lavender)}
.pkg-photo{position:absolute;top:97px;width:326px;height:248px}
.pkg-card{position:absolute;top:295px;width:279px;height:257px;background:var(--white);box-shadow:0 6px 18px rgba(30,37,82,.12);padding:22px 0 0 39px;color:var(--ink)}
.pkg-card.featured{background:var(--navy);color:var(--white)}
.pkg-card h3{font-family:'Open Sans',sans-serif;font-size:23px;font-weight:600}
.pkg-card .line{font-size:12px;margin-top:12px;line-height:15px}
.pkg-card .row{display:flex;justify-content:space-between;width:210px}
.pkg-card .book{display:flex;align-items:center;justify-content:center;margin-top:12px;width:139px;height:36px;background:var(--green);color:var(--white);font-size:13px;font-weight:600}

/* care */
.care{position:absolute;left:0;top:2463px;width:1200px;height:537px;background:linear-gradient(135deg,#8ccc12 0%,#a4d923 55%,#b9e23a 100%);overflow:hidden}
.care svg.photo{position:absolute;left:0;top:0}
.care h2{position:absolute;left:108px;top:71px;font-size:30px;font-weight:700;color:var(--white)}
.care-item{position:absolute;left:190px;color:var(--white)}
.care-item h3{font-family:'Montserrat',sans-serif;font-size:20px;font-weight:600}
.care-item p{margin-top:6px;font-size:12.5px;line-height:18px;width:340px;color:#f4fbe4}

/* why */
.why{position:absolute;left:0;top:3000px;width:1200px;height:522px;background:var(--white)}
.video{position:absolute;left:108px;top:97px;width:463px;height:320px;background:linear-gradient(160deg,#6a6f78 0%,#3e3f44 55%,#2a2624 100%)}
.why h2{position:absolute;left:622px;top:102px;font-size:30px;font-weight:700;color:var(--ink)}
.why p{position:absolute;left:622px;width:520px;font-size:14.5px;line-height:23px;color:#3d4158}
.btn-green{left:622px;top:353px;width:178px;height:46px;background:var(--green);color:var(--white)}

/* benefits */
.benefits{position:absolute;left:0;top:3522px;width:1200px;height:463px;background:linear-gradient(135deg,#1c2350 0%,#263066 60%,#1e2658 100%)}
.benefits h2{position:absolute;left:0;top:62px;width:1200px;text-align:center;font-size:29px;font-weight:700;color:var(--white)}
.benefit-list{position:absolute;top:146px;list-style:none}
.benefit-list li{display:flex;align-items:center;gap:14px;height:34.3px;font-size:19px;font-weight:300;color:var(--white)}

/* footer */
.site-footer{position:absolute;left:0;top:3985px;width:1200px;height:433px;background:var(--white)}
.foot-brand{position:absolute;left:100px;top:76px;display:flex;align-items:center;gap:12px}
.foot-about{position:absolute;left:110px;top:162px;width:330px;font-size:13px;line-height:18px;color:#4a4e66}
.social{position:absolute;top:238px;width:14px;height:14px;border-radius:50%;background:var(--navy)}
.foot-col{position:absolute;top:68px}
.foot-col h4{font-size:20px;font-weight:700;color:var(--ink);margin-bottom:12px}
.foot-col a{display:block;font-size:15px;line-height:28px;color:#3d4158;text-decoration:none}
.contact-row{display:flex;align-items:center;gap:10px;font-size:15px;line-height:28px;color:#3d4158}
.contact-row.indent{padding-left:28px}
.foot-rule{position:absolute;left:99px;top:354px;width:986px;height:1px;background:#cfd1dc}
.copyright{position:absolute;left:0;top:377px;width:1200px;text-align:center;font-size:12px;color:#4a4e66}
</style>
</head>
<body>

<header class="site-header">
  <div class="brand"><span class="brand-dot"></span><span class="brand-name">Maplecrest Drip Clinic</span></div>
  <nav class="main-nav">
    <a class="active" style="left:403px" href="#">Services</a>
    <a style="left:509px" href="#">Intake Forms</a>
    <a style="left:646px" href="#">Products</a>
    <a style="left:752px" href="#">Our Team</a>
    <a style="left:866px" href="#">Book Online</a>
    <a style="left:1001px" href="#">Contact Us</a>
  </nav>
  <svg class="cart" width="36" height="34" viewBox="0 0 36 34" aria-label="Cart">
    <path d="M2 6h5l4 15h15l4-11H9" fill="none" stroke="#23284a" stroke-width="2.4" stroke-linejoin="round"/>
    <circle cx="13" cy="27" r="2.4" fill="#23284a"/><circle cx="24" cy="27" r="2.4" fill="#23284a"/>
    <circle cx="28" cy="5" r="5" fill="#8fcb18"/><text x="28" y="8" font-size="7" text-anchor="middle" fill="#fff" font-family="Montserrat,sans-serif">0</text>
  </svg>
</header>

<section class="hero" role="img" aria-label="Photo of two clients relaxing in recliners during IV infusion">
  <div class="hero-shade"></div>
  <svg class="arrow" style="left:26px" width="28" height="44" viewBox="0 0 28 44"><path d="M22 4L6 22l16 18" fill="none" stroke="#fff" stroke-width="4"/></svg>
  <svg class="arrow" style="left:1148px" width="28" height="44" viewBox="0 0 28 44"><path d="M6 4l16 18L6 40" fill="none" stroke="#fff" stroke-width="4"/></svg>
  <h1 class="hero-title">Maplecrest <span>Drip Clinic</span></h1>
  <div class="hero-sub">Natural Health &amp; Wellness</div>
  <p class="hero-text">Curabitur vel mi sit amet magna malesuada ultrices<br>Ut nisi erat fermentum vel congue euismod</p>
  <a class="btn btn-outline-green" href="#">Learn More</a>
</section>

<section class="welcome">
  <div class="welcome-photo" role="img" aria-label="Photo of a young client seated for treatment"></div>
  <h2>Welcome to Maplecrest Drip Clinic</h2>
  <div class="tagline">Natural Health &amp; Wellness</div>
  <p>Our team offers a full spectrum of healing modalities to optimize your physical, emotional and spiritual well being.<br>Check out our list of treatments and services below.<br>Curabitur vel mi sit amet magna malesuada ultrices Ut nisi erat fermentum vel congue id euismod in elit Fusce ultricies</p>
  <a class="btn btn-outline-navy" href="#">Learn More</a>
</section>

<section class="services">
  <h2>Our Services</h2>
  <div class="service" style="left:74px">
    <svg width="82" height="118" viewBox="0 0 82 118"><circle cx="41" cy="74" r="39" fill="#8fcb18"/><path d="M41 56c-10 0-14 8-14 14s6 10 10 12v8h8v-8c4-2 10-6 10-12s-4-14-14-14z" fill="#fff"/></svg>
    <h3>IV Nutrition Therapy</h3>
    <p>Direct infusion of vitamins and minerals, like high doses of vitamin C or magnesium.a</p>
  </div>
  <div class="service" style="left:341px">
    <svg width="82" height="118" viewBox="0 0 82 118"><circle cx="41" cy="74" r="39" fill="#8fcb18"/><path d="M35 56h12M37 56v14l-10 18h28L45 70V56" fill="none" stroke="#fff" stroke-width="3.5" stroke-linejoin="round"/></svg>
    <h3>Lab Services</h3>
    <p>We provide our clients with access to over 6000 individual tests, test panels.</p>
  </div>
  <div class="service" style="left:609px">
    <svg width="82" height="118" viewBox="0 0 82 118"><circle cx="41" cy="74" r="39" fill="#8fcb18"/><rect x="29" y="58" width="24" height="32" rx="3" fill="none" stroke="#fff" stroke-width="3"/><path d="M35 56h12M34 70h14M34 77h14M34 84h10" stroke="#fff" stroke-width="2.5"/></svg>
    <h3>Health Report</h3>
    <p>Reports convert standard lab results to uncover dysfunction areas from a functional health perspective.</p>
  </div>
  <div class="service" style="left:876px">
    <svg width="82" height="118" viewBox="0 0 82 118"><circle cx="41" cy="74" r="39" fill="#8fcb18"/><circle cx="41" cy="74" r="7" fill="none" stroke="#fff" stroke-width="3"/><path d="M41 58v7M41 83v7M25 74h7M50 74h7M30 63l5 5M47 80l5 5M52 63l-5 5M35 80l-5 5" stroke="#fff" stroke-width="3"/></svg>
    <h3>Pulse Laser Therapy</h3>
    <p>Class IV Laser manages pain and inflammation while accelerating tissue regeneration</p>
  </div>
  <a class="btn btn-outline-white" href="#">View More</a>
</section>

<section class="packages">
  <div class="pkg-photo" style="left:94px;background:linear-gradient(160deg,#8c8780,#3b3a3c)" role="img" aria-label="Photo of a client seated on a leather couch"></div>
  <div class="pkg-photo" style="left:442px;background:linear-gradient(160deg,#d7c8a8,#5a2f2c)" role="img" aria-label="Photo of clients in recliners receiving infusions"></div>
  <div class="pkg-photo" style="left:800px;background:linear-gradient(160deg,#cdbb94,#4d2a2a)" role="img" aria-label="Photo of a nurse preparing an infusion for a client"></div>

  <div class="pkg-card" style="left:117px">
    <h3>4 Pack ivs</h3>
    <div class="line">Any four IV Infusions</div>
    <div class="line">Regular price $175 ea</div>
    <div class="line row"><span>Total Package Value<br>savings)</span><span>$700 ($200</span></div>
    <div class="line">Your price&nbsp; $125 each</div>
    <div class="book">BOOK NOW</div>
  </div>
  <div class="pkg-card featured" style="left:464px;top:297px">
    <h3>6 pack ivs</h3>
    <div class="line">Any Six IV Infusions</div>
    <div class="line">Regular price $175 ea</div>
    <div class="line row"><span>Total Package Value<br>savings)</span><span>$1050 ($390</span></div>
    <div class="line">Your price - $110 each</div>
    <div class="book">BOOK NOW</div>
  </div>
  <div class="pkg-card" style="left:823px">
    <h3>12 Pack ivs</h3>
    <div class="line">Any twelve IV infusions</div>
    <div class="line">Regular price $175 ea</div>
    <div class="line row"><span>Total Package Value<br>savings)</span><span>$2100 ($900</span></div>
    <div class="line">Your price - $100 each</div>
    <div class="book">BOOK NOW</div>
  </div>
</section>

<section class="care">
  <svg class="photo" width="1200" height="537" viewBox="0 0 1200 537" role="img" aria-label="Photo of staff and clients in the infusion lounge">
    <defs><linearGradient id="careFill" x1="0" y1="0" x2="1" y2="1"><stop offset="0" stop-color="#c9b8a0"/><stop offset=".5" stop-color="#6b2a2c"/><stop offset="1" stop-color="#3a2a2a"/></linearGradient></defs>
    <path d="M700 0 C 590 140 520 300 560 537 H1200 V0 Z" fill="url(#careFill)"/>
    <path d="M700 0 C 590 140 520 300 560 537" fill="none" stroke="#fff" stroke-width="8"/>
  </svg>
  <h2>Taking Care of your health</h2>
  <div class="care-item" style="top:158px"><h3>Functional Health Report</h3><p>A Functional Health Report takes your lab data and analyzes it to help you understand what's going</p></div>
  <div class="care-item" style="top:268px"><h3>Online Dispensary</h3><p>Nutraceuticals - Online Store<br>Pharmaceutical Grade Supplements</p></div>
  <div class="care-item" style="top:376px"><h3>Laboratory Services</h3><p>We provide the industry's most advanced diagnostic services and solutions - so you can make better healthcare decisions.</p></div>
</section>

<section class="why">
  <div class="video" role="img" aria-label="Video preview of the clinic lounge interior">
    <svg class="abs" style="left:193px;top:122px" width="78" height="78" viewBox="0 0 78 78"><circle cx="39" cy="39" r="35" fill="none" stroke="#fff" stroke-width="5"/><path d="M31 24l22 15-22 15z" fill="#fff"/></svg>
  </div>
  <h2>Why IV Therapy</h2>
  <p style="top:160px">Augiat in pede Fusce tellus Sed metus augue convallis et vehicula ut pulvinar eu ante Integer orci tellus tristique vitae consequat</p>
  <p style="top:238px">ultricies orci ac feugiat suscipit leo massa sodales velit et scelerisque mi tortor at ipsum Proin orci odio commodo ac gravida non tristique vel te Curabitur iaculis tempus eros Curabitur vel mi sit amet magna malesuada ultrices Ut nisi erat fermentum vel congue</p>
  <a class="btn btn-green" href="#">Learn More</a>
</section>

<section class="benefits">
  <h2>Benefits of IV Therapy?</h2>
  <ul class="benefit-list" style="left:164px">
    <li><svg width="20" height="20" viewBox="0 0 20 20"><circle cx="10" cy="10" r="8" fill="none" stroke="#8fcb18" stroke-width="2"/><path d="M6 10l3 3 7-7" fill="none" stroke="#8fcb18" stroke-width="2.2"/></svg>100% absorption</li>
    <li><svg width="20" height="20" viewBox="0 0 20 20"><circle cx="10" cy="10" r="8" fill="none" stroke="#8fcb18" stroke-width="2"/><path d="M6 10l3 3 7-7" fill="none" stroke="#8fcb18" stroke-width="2.2"/></svg>Aids in weight loss</li>
    <li><svg width="20" height="20" viewBox="0 0 20 20"><circle cx="10" cy="10" r="8" fill="none" stroke="#8fcb18" stroke-width="2"/><path d="M6 10l3 3 7-7" fill="none" stroke="#8fcb18" stroke-width="2.2"/></svg>Allowed by all major athletic associations</li>
    <li><svg width="20" height="20" viewBox="0 0 20 20"><circle cx="10" cy="10" r="8" fill="none" stroke="#8fcb18" stroke-width="2"/><path d="M6 10l3 3 7-7" fill="none" stroke="#8fcb18" stroke-width="2.2"/></svg>Boosts immune system</li>
    <li><svg width="20" height="20" viewBox="0 0 20 20"><circle cx="10" cy="10" r="8" fill="none" stroke="#8fcb18" stroke-width="2"/><path d="M6 10l3 3 7-7" fill="none" stroke="#8fcb18" stroke-width="2.2"/></svg>Counteracts stress</li>
    <li><svg width="20" height="20" viewBox="0 0 20 20"><circle cx="10" cy="10" r="8" fill="none" stroke="#8fcb18" stroke-width="2"/><path d="M6 10l3 3 7-7" fill="none" stroke="#8fcb18" stroke-width="2.2"/></svg>Detoxifies cells</li>
  </ul>
  <ul class="benefit-list" style="left:652px">
    <li><svg width="20" height="20" viewBox="0 0 20 20"><circle cx="10" cy="10" r="8" fill="none" stroke="#8fcb18" stroke-width="2"/><path d="M6 10l3 3 7-7" fill="none" stroke="#8fcb18" stroke-width="2.2"/></svg>Fast, lasting results</li>
    <li><svg width="20" height="20" viewBox="0 0 20 20"><circle cx="10" cy="10" r="8" fill="none" stroke="#8fcb18" stroke-width="2"/><path d="M6 10l3 3 7-7" fill="none" stroke="#8fcb18" stroke-width="2.2"/></svg>High doses not tolerated orally</li>
    <li><svg width="20" height="20" viewBox="0 0 20 20"><circle cx="10" cy="10" r="8" fill="none" stroke="#8fcb18" stroke-width="2"/><path d="M6 10l3 3 7-7" fill="none" stroke="#8fcb18" stroke-width="2.2"/></svg>Improves athletic performance</li>
    <li><svg width="20" height="20" viewBox="0 0 20 20"><circle cx="10" cy="10" r="8" fill="none" stroke="#8fcb18" stroke-width="2"/><path d="M6 10l3 3 7-7" fill="none" stroke="#8fcb18" stroke-width="2.2"/></svg>Instantly reverses dehydration, pain &amp; fatigue</li>
    <li><svg width="20" height="20" viewBox="0 0 20 20"><circle cx="10" cy="10" r="8" fill="none" stroke="#8fcb18" stroke-width="2"/><path d="M6 10l3 3 7-7" fill="none" stroke="#8fcb18" stroke-width="2.2"/></svg>Lifts mood naturally</li>
    <li><svg width="20" height="20" viewBox="0 0 20 20"><circle cx="10" cy="10" r="8" fill="none" stroke="#8fcb18" stroke-width="2"/><path d="M6 10l3 3 7-7" fill="none" stroke="#8fcb18" stroke-width="2.2"/></svg>Medically-supervised facility</li>
  </ul>
</section>

<footer class="site-footer">
  <div class="foot-brand"><span class="brand-dot" style="width:44px;height:44px"></span><span class="brand-name" style="font-size:28px">Maplecrest Drip Clinic</span></div>
  <p class="foot-about">Lorem ipsum dolor sit amet consectetuer adipiscing elit Nam cursus Morbi ut mi Nullam enim leo egestas dolor sit amet consec</p>
  <span class="social" style="left:113px"></span>
  <span class="social" style="left:168px"></span>
  <span class="social" style="left:223px"></span>
  <span class="social" style="left:278px"></span>

  <div class="foot-col" style="left:492px"><h4>Quick links</h4><a href="#" style="padding-left:5px">About Us</a><a href="#" style="padding-left:5px">Services</a><a href="#" style="padding-left:5px">Intake Forms</a><a href="#" style="padding-left:5px">Products</a></div>
  <div class="foot-col" style="left:674px"><h4>Resources</h4><a href="#" style="padding-left:5px">Our Team</a><a href="#" style="padding-left:5px">Book Online</a><a href="#" style="padding-left:5px">Contact Us</a></div>
  <div class="foot-col" style="left:840px"><h4>Contact Us</h4>
    <div class="contact-row"><svg width="18" height="20" viewBox="0 0 18 20"><path d="M9 1a7 7 0 0 0-7 7c0 5 7 11 7 11s7-6 7-11a7 7 0 0 0-7-7z" fill="#8fcb18"/><circle cx="9" cy="8" r="2.6" fill="#fff"/></svg>418 Birchfield Commons Rd.</div>
    <div class="contact-row indent">Lakeview, FL 32790</div>
    <div class="contact-row"><svg width="18" height="18" viewBox="0 0 18 18"><path d="M4 1l3 4-2 2c1 3 3 5 6 6l2-2 4 3-2 3C8 17 1 10 1 3z" fill="#8fcb18"/></svg>555.014.2297</div>
    <div class="contact-row"><svg width="18" height="14" viewBox="0 0 18 14"><rect x="0" y="0" width="18" height="14" rx="1.5" fill="#8fcb18"/><path d="M1 1l8 7 8-7" fill="none" stroke="#fff" stroke-width="1.6"/></svg>hello@maplecrestdripcare.com</div>
  </div>
  <div class="foot-rule"></div>
  <div class="copyright">© 2020 Company Name | All Rights Reserved</div>
</footer>

</body>
</html>
```